Varlow's Electrical & Solar - Business Cards

I want my business card to stand out from the rest. I will provide my business name logo and my icon logo to be implemented onto the card.

On the front of the card, can i have the following. Just make it neat & professional please.

Dean Harrop
varlowselectrical@mailbox-example.net
0491 837 562
ABN: 41 269 507 813
License No. 582146K
FREE QUOTES
24/7 Emergency

On the back of the card, can I have "Our Services" and maybe add the V logo on the back in the background or something. Under "Our Services" I want the following:

LED Lighting Upgrades
Switches & Outlets
Smoke Alarms
Switchboard Upgrades
Fault Finding
Rewiring
New Builds
Test & Tagging
All Electrical Maintenance & Repairs

Can you guys add the instagram logo and next to it, put varlows_electrical

Can you guys also add the facebook logo and next to it put Varlow's Electrical & Solar. Make sure the instagram & facebook icon is in either white, green or black.

Also I have put down double sided, not sure why when i save it, it keeps going to single sided. I need my business card double sided.

New Customers

Dean Harrop varlowselectrical@mailbox-example.net 0491 837 562 ABN: 41 269 507 813 License No. 582146K FREE QUOTES 24/7 Emergency

• must be tidy, professional and appealing

```html
<!DOCTYPE html>
<html lang="en">
<head>
<meta charset="utf-8">
<title>Varlow's Electrical &amp; Solar – Business Cards</title>
<link rel="stylesheet" href="https://fonts.googleapis.com/css2?family=Montserrat:wght@400;500;700;800&display=swap">
<style>
  :root {
    --bg: #2b2b2d;
    --card: #111213;
    --green: #3dba4e;
    --white: #f2f2f2;
    --grey: #d9d9d9;
  }
  * { margin: 0; padding: 0; box-sizing: border-box; }
  html, body { width: 1200px; height: 913px; overflow: hidden; background: var(--bg); }
  body { position: relative; font-family: 'Montserrat', sans-serif; color: var(--white); }

  .card {
    position: absolute;
    left: 280px;
    width: 640px;
    height: 366px;
    background: var(--card);
    border-radius: 22px;
    border-bottom: 4px solid var(--green);
    border-left: 2px solid var(--green);
    overflow: hidden;
  }
  .card-back { top: 70px; }
  .card-front { top: 477px; }

  /* Back: services */
  .services-title {
    position: absolute; left: 44px; top: 56px;
    font-weight: 800; font-size: 24px; color: var(--green); letter-spacing: 0.5px;
  }
  .services-list {
    position: absolute; left: 48px; top: 100px;
    list-style: none; font-size: 17px; font-weight: 500; line-height: 27px;
  }
  .services-list li::before {
    content: ""; display: inline-block; width: 7px; height: 7px;
    border-radius: 50%; background: var(--green); margin-right: 9px; vertical-align: middle;
  }
  .brand-mark {
    position: absolute; left: 360px; top: 28px;
    width: 240px; height: 240px; border-radius: 50%;
    border: 12px solid var(--green);
    display: flex; align-items: center; justify-content: center;
    font-weight: 800; font-size: 36px; color: var(--grey);
  }

  /* Front: contact */
  .brand-name {
    position: absolute; left: 0; right: 0; top: 62px; text-align: center;
    font-weight: 800; font-size: 30px; color: var(--grey); letter-spacing: 0.5px;
  }
  .contact {
    position: absolute; right: 308px; top: 170px; text-align: right;
  }
  .contact-name { font-weight: 800; font-size: 26px; color: var(--green); margin-bottom: 8px; }
  .contact-line {
    display: flex; align-items: center; justify-content: flex-end; gap: 8px;
    font-size: 17px; line-height: 28px; white-space: nowrap;
  }
  .contact-line.email { font-size: 13.5px; }
  .icon { width: 15px; height: 15px; fill: var(--green); flex: none; }
  .divider {
    position: absolute; left: 350px; top: 170px; width: 2px; height: 110px; background: var(--green);
  }
  .details {
    position: absolute; left: 372px; top: 174px; font-size: 17px; line-height: 25px; white-space: nowrap;
  }
  .details .highlight { color: var(--green); font-weight: 700; }

  .social {
    position: absolute; left: 0; right: 0; top: 312px;
    display: flex; justify-content: center; gap: 36px;
    font-size: 13px; font-weight: 500; color: var(--grey);
  }
  .social-item { display: flex; align-items: center; gap: 8px; white-space: nowrap; }
  .social-dot { width: 14px; height: 14px; border-radius: 50%; background: var(--green); flex: none; }
</style>
</head>
<body>

<section class="card card-back" aria-label="Back of card">
  <h2 class="services-title">OUR SERVICES</h2>
  <ul class="services-list">
    <li>LED Lighting Upgrades</li>
    <li>Switches &amp; Outlets</li>
    <li>Smoke Alarms</li>
    <li>Switchboard Upgrades</li>
    <li>Fault Finding</li>
    <li>Rewiring</li>
    <li>New Builds</li>
    <li>Test &amp; Tagging</li>
    <li>All Electrical Maintenance &amp; Repairs</li>
  </ul>
  <div class="brand-mark">Varlow's</div>
</section>

<section class="card card-front" aria-label="Front of card">
  <div class="brand-name">Varlow's Electrical &amp; Solar</div>

  <div class="contact">
    <div class="contact-name">DEAN HARROP</div>
    <div class="contact-line">0491 837 562
      <svg class="icon" viewBox="0 0 24 24" aria-hidden="true"><path d="M6.6 10.8a15.1 15.1 0 0 0 6.6 6.6l2.2-2.2a1 1 0 0 1 1-.25 11.4 11.4 0 0 0 3.6.57 1 1 0 0 1 1 1V20a1 1 0 0 1-1 1A17 17 0 0 1 3 4a1 1 0 0 1 1-1h3.5a1 1 0 0 1 1 1c0 1.25.2 2.45.57 3.6a1 1 0 0 1-.25 1z"/></svg>
    </div>
    <div class="contact-line email">varlowselectrical@mailbox-example.net
      <svg class="icon" viewBox="0 0 24 24" aria-hidden="true"><path d="M2 5h20v14H2z M2 5l10 8 10-8" fill="none" stroke="#3dba4e" stroke-width="2"/></svg>
    </div>
  </div>

  <div class="divider"></div>

  <div class="details">
    <div>ABN: 41 269 507 813</div>
    <div>License No. 582146K</div>
    <div class="highlight">FREE QUOTES</div>
    <div><span class="highlight">24/7</span> Emergency</div>
  </div>

  <div class="social">
    <div class="social-item"><span class="social-dot" aria-hidden="true"></span>varlows_electrical</div>
    <div class="social-item"><span class="social-dot" aria-hidden="true"></span>Varlow's Electrical &amp; Solar</div>
  </div>
</section>

</body>
</html>
```